Wordpress website re-design

Update existing 5 page wordpress website to look more professional. We run a 10 week boxing program that ends in a black tie gala event.

We would like to keep the existing pink hero colour.

The website:
- must be Wordpress
- prefer it to work with the Elementor plugin for easy future changes
- Keep the existing URL structure
- Use white space/backgrounds - D not want all black background or the pink colour used as the background for an entire section
- Shouldn't look too 'templatey'. Good flow between sections

Logo, images and video to use can be found here: https://share.quorvexfiles.net/folders/8hTqzW2mLpRvBn4kXcYd_JsEaGfUoNiM-?view=public

Website to be redesigned: https://bellmoreshowcase.com.au/

Designs look the same

Target Market(s)

Men working office jobs aged 28-38

Coding

Coded - Design and coding required

Number of Pages Required

5+ page

Colors

Designer to choose colors to be used in the design.

Requirements
Must have
• Wordpress
Nice to have
• Work with Elementor so that I can easily make changes in the future
Should not have
• Entirely black background. Want it to be lighter / plenty of white background. Not too blocky - flowing through sections and some of the images with backgrounds removed to make it less blocky also. I do not want it to be clerly 'templatey'. The pink should be used as a hero colour, not for entire sections

```html
<!DOCTYPE html>
<html lang="en">
<head>
<meta charset="utf-8">
<title>Bellmore Showcase – Boxing Program</title>
<link rel="stylesheet" href="https://fonts.googleapis.com/css2?family=Bebas+Neue&family=Poppins:wght@400;500;600&display=swap">
<style>
:root{
  --pink:#ec0a6e;
  --pink-soft:#fde4ef;
  --ink:#141414;
  --text:#3a3a3a;
  --muted:#666;
  --light:#f6f6f7;
  --line:#e2e2e4;
  --white:#fff;
  --footer:#1a1a1a;
  --head:'Bebas Neue',Impact,sans-serif;
  --body:'Poppins',Arial,sans-serif;
}
*{box-sizing:border-box;margin:0;padding:0}
html,body{width:1200px;height:4739px;overflow:hidden;background:var(--white);color:var(--text);font-family:var(--body)}
.page{position:relative;width:1200px;height:4739px;background:var(--white)}
.abs{position:absolute}
h1,h2,h3{font-family:var(--head);font-weight:400;letter-spacing:.5px;color:var(--ink)}

/* top bar */
.topbar{left:0;top:0;width:1200px;height:30px;background:var(--pink);color:var(--white);font-size:13px;display:flex;align-items:center;justify-content:space-between;padding:0 100px;white-space:nowrap}
.topbar .follow{display:flex;align-items:center;gap:6px}
.dot{width:20px;height:20px;border-radius:50%;background:var(--white);display:inline-block}

/* nav */
.nav{left:0;top:30px;width:1200px;height:86px;background:var(--white);border-bottom:1px solid var(--line);display:flex;align-items:center;padding:0 100px;white-space:nowrap}
.brand{display:flex;align-items:center;gap:8px;font-weight:600;font-size:17px;line-height:1.05;text-transform:uppercase;width:200px;color:var(--ink)}
.brand .sq{width:14px;height:14px;background:var(--pink)}
.menu{display:flex;gap:20px;margin-left:26px;font-size:15px;text-transform:uppercase;color:var(--ink)}
.menu .active{color:var(--pink);position:relative}
.menu .active::after{content:"";position:absolute;left:50%;top:24px;width:10px;height:10px;margin-left:-5px;border-radius:50%;background:var(--pink)}
.btn-pink{background:var(--pink);color:var(--white);font-weight:600;font-size:15px;text-transform:uppercase;padding:8px 28px;margin-left:auto;white-space:nowrap}

/* hero */
.hero{left:0;top:116px;width:1200px;height:626px;background:radial-gradient(ellipse at 70% 40%,#34406e 0%,#1a1c2e 45%,#0b0b10 100%)}
.hero-photo{position:absolute;inset:0;background:linear-gradient(100deg,rgba(60,10,20,.55) 0%,rgba(150,20,30,.35) 45%,rgba(20,50,140,.45) 75%,rgba(10,10,20,.4) 100%)}
.hero-copy{position:absolute;left:99px;top:170px;width:470px;color:var(--white)}
.hero-copy h1{font-size:52px;line-height:48px;color:var(--white)}
.hero-copy p{font-size:14.5px;line-height:26px;margin:14px 0 18px}
.btn-small{display:inline-block;background:var(--pink);color:var(--white);font-weight:600;font-size:14px;padding:7px 26px;text-transform:uppercase}
.dots{position:absolute;left:555px;top:576px;display:flex;gap:8px}
.dots span{width:12px;height:12px;border-radius:50%;background:var(--white)}
.dots span:first-child{outline:2px solid var(--white);outline-offset:2px}

.sec-title{position:absolute;left:0;width:1200px;text-align:center;font-size:42px}

/* video */
.video{left:259px;top:881px;width:681px;height:381px;background:linear-gradient(90deg,#1c1c2a,#5a2a30 40%,#2c3d78 75%,#15151e);box-shadow:0 0 30px rgba(236,10,110,.4)}
.play{position:absolute;left:50%;top:50%;width:70px;height:70px;margin:-35px 0 0 -35px}

/* why */
.why-bg{left:0;top:1343px;width:1200px;height:530px;background:var(--light)}
.why-img{left:560px;top:1343px;width:640px;height:530px;background:linear-gradient(135deg,#0d1233,#1e2b66 50%,#5c1620 100%);clip-path:polygon(12.5% 0,100% 0,100% 100%,5.3% 100%)}
.why-edge{left:0;top:1343px;width:640px;height:530px}
.why-copy{left:99px;top:1408px;width:470px;font-size:14.5px;line-height:28px;color:var(--text)}
.why-copy h2{font-size:40px;margin-bottom:8px}
.why-copy h2 em{font-style:normal;color:var(--pink)}
.why-copy ul{list-style:none;margin:8px 0 22px}
.why-copy li::before{content:"";display:inline-block;width:7px;height:7px;background:var(--pink);margin-right:10px;vertical-align:middle}
.btn-outline{display:inline-block;border:2px solid var(--pink);color:var(--pink);font-weight:500;font-size:14px;padding:6px 26px;text-transform:uppercase}

/* cards */
.card{width:317px;height:323px;background:var(--white);border:1px solid var(--line);border-top:4px solid var(--pink);box-shadow:0 6px 20px rgba(236,10,110,.12);text-align:center;padding-top:30px}
.card h3{font-size:26px;line-height:27px;margin:12px 0 14px}
.card p{font-size:13.5px;line-height:27px;color:var(--muted);padding:0 24px}
.chev{display:block;margin:12px auto 0}

/* black tie */
.tie-bg{left:0;top:2793px;width:1200px;height:528px;background:var(--light)}
.tie-img{left:0;top:2793px;width:561px;height:528px;background:linear-gradient(120deg,#6a5a52,#7a1a1e 55%,#1a1010);clip-path:polygon(0 0,100% 0,93.6% 100%,0 100%)}
.tie-edge{left:520px;top:2793px;width:60px;height:528px}
.tie-copy{left:642px;top:2857px;width:460px;font-size:13px;line-height:24px;color:var(--text)}
.tie-copy h2{font-size:42px;line-height:46px;margin-bottom:10px}
.tie-copy p{margin-bottom:8px;text-align:justify}
.tie-copy .meta{color:var(--ink);font-weight:500}

/* follow grid */
.tile{width:240px;height:177px}

/* contact */
.contact{left:0;top:3947px;width:1200px;height:469px;background:var(--light);border-top:4px solid var(--pink)}
.contact h2{position:absolute;left:0;top:70px;width:1200px;text-align:center;font-size:44px}
.contact .sub{position:absolute;left:0;top:117px;width:1200px;text-align:center;font-size:15px;color:var(--muted)}
.field{position:absolute;background:var(--white);border:1px solid var(--line);color:#555;font-size:14px;padding:16px 18px}
.submit{position:absolute;left:523px;top:366px;width:154px;height:40px;background:var(--pink);color:var(--white);text-align:center;line-height:40px;font-weight:600;font-size:14px}

/* footer */
.footer{left:0;top:4416px;width:1200px;height:323px;background:var(--footer);color:var(--white)}
.foot-brand{position:absolute;left:128px;top:60px;width:190px;height:130px;border:4px solid var(--pink);display:flex;align-items:center;justify-content:center;text-align:center;font-weight:600;font-size:24px;line-height:28px;text-transform:uppercase}
.foot-social{position:absolute;left:140px;top:214px;display:flex;gap:9px}
.foot-social span{width:34px;height:34px;border-radius:50%;border:2px solid var(--white)}
.col{position:absolute;top:66px;font-size:13px;line-height:24px}
.col h4{font-weight:500;font-size:17px;margin-bottom:14px;text-transform:uppercase}
.col .row{display:flex;gap:6px;align-items:flex-start;margin-bottom:12px}
.news-input{margin-top:14px;width:296px;height:36px;border:1px solid var(--white);display:flex;justify-content:space-between;align-items:center;padding-left:12px}
.news-input .go{width:36px;height:36px;background:var(--pink);display:flex;align-items:center;justify-content:center}
.rule{position:absolute;left:100px;top:266px;width:1000px;height:1px;background:#444}
.copy{position:absolute;left:0;top:276px;width:1200px;text-align:center;font-size:13px}
</style>
</head>
<body>
<div class="page">

  <div class="abs topbar">
    <span>✉ hello@bellmoreshowcase.com.au</span>
    <span class="follow">Follow On <i class="dot"></i><i class="dot"></i><i class="dot"></i></span>
  </div>

  <nav class="abs nav">
    <div class="brand"><span class="sq"></span>Bellmore<br>Showcase</div>
    <div class="menu">
      <span class="active">Home</span><span>About The Program</span><span>Meet The Team</span><span>Past Fighters</span><span>Contact Us</span>
    </div>
    <span class="btn-pink">Join Now</span>
  </nav>

  <section class="abs hero">
    <div class="hero-photo" role="img" aria-label="Two amateur boxers in red and blue exchanging punches in the ring under arena lights"></div>
    <div class="hero-copy">
      <h1>From Desk To The Ring<br>In 10 Weeks!</h1>
      <p>We help people like you go from little or no boxing experience to a boxing bout in 10 weeks. Get fit, have fun and support charity in a safe environment.</p>
      <span class="btn-small">Join Now</span>
    </div>
    <div class="dots"><span></span><span></span><span></span><span></span></div>
  </section>

  <h2 class="sec-title" style="top:805px">Take A Look At Your Next Experience</h2>
  <div class="abs video" role="img" aria-label="Video still of a referee raising the winning boxer's arm in the ring">
    <svg class="play" viewBox="0 0 70 70"><circle cx="35" cy="35" r="32" fill="rgba(0,0,0,.35)" stroke="#fff" stroke-width="4"/><path d="M28 21 L50 35 L28 49 Z" fill="#fff"/></svg>
  </div>

  <div class="abs why-bg"></div>
  <div class="abs why-img" role="img" aria-label="Boxer in blue headgear landing a punch on an opponent in red"></div>
  <svg class="abs why-edge" viewBox="0 0 640 530"><polygon points="628,0 640,0 594,530 582,530" fill="#ec0a6e"/></svg>
  <div class="abs why-copy">
    <h2>Why <em>Bellmore Showcase?</em></h2>
    <p>If getting fit, supporting charity and having a good time in a safe environment sound appealing, then this program is the program for you.</p>
    <ul>
      <li>Lose weight and get fit</li>
      <li>Fight in front of friends, family and coworkers at the exclusive black tie dinner</li>
      <li>Learn valuable boxing skills</li>
      <li>Build friendships with your fellow fighters</li>
    </ul>
    <span class="btn-outline">Learn More</span>
  </div>

  <h2 class="sec-title" style="top:1940px">What's Included?</h2>
  <div class="abs" style="left:99px;top:2020px;width:1001px;height:672px">
    <div style="display:grid;grid-template-columns:317px 317px 317px;column-gap:26px;row-gap:26px">
      <div class="card"><svg width="52" height="52" viewBox="0 0 52 52"><circle cx="26" cy="26" r="24" fill="#fde4ef"/><g stroke="#ec0a6e" stroke-width="3" stroke-linecap="round"><line x1="17" y1="35" x2="35" y2="17"/><line x1="12" y1="32" x2="20" y2="40"/><line x1="32" y1="12" x2="40" y2="20"/></g></svg><h3>3 Weekly Training Sessions<br>For 10 Weeks</h3><p>Training takes place each Tuesday, Thursday and Saturday throughout the 10 week program.</p><svg class="chev" width="34" height="34" viewBox="0 0 34 34"><circle cx="17" cy="17" r="17" fill="#ec0a6e"/><path d="M11 14 L17 20 L23 14" stroke="#fff" stroke-width="3" fill="none"/></svg></div>
      <div class="card"><svg width="52" height="52" viewBox="0 0 52 52"><circle cx="26" cy="26" r="24" fill="#fde4ef"/><g stroke="#ec0a6e" stroke-width="3" stroke-linecap="round"><line x1="17" y1="35" x2="35" y2="17"/><line x1="12" y1="32" x2="20" y2="40"/><line x1="32" y1="12" x2="40" y2="20"/></g></svg><h3>3 Weekly Training Sessions<br>For 10 Weeks</h3><p>Training takes place each Tuesday, Thursday and Saturday throughout the 10 week program.</p><svg class="chev" width="34" height="34" viewBox="0 0 34 34"><circle cx="17" cy="17" r="17" fill="#ec0a6e"/><path d="M11 14 L17 20 L23 14" stroke="#fff" stroke-width="3" fill="none"/></svg></div>
      <div class="card"><svg width="52" height="52" viewBox="0 0 52 52"><circle cx="26" cy="26" r="24" fill="#fde4ef"/><g stroke="#ec0a6e" stroke-width="3" stroke-linecap="round"><line x1="17" y1="35" x2="35" y2="17"/><line x1="12" y1="32" x2="20" y2="40"/><line x1="32" y1="12" x2="40" y2="20"/></g></svg><h3>3 Weekly Training Sessions<br>For 10 Weeks</h3><p>Training takes place each Tuesday, Thursday and Saturday throughout the 10 week program.</p><svg class="chev" width="34" height="34" viewBox="0 0 34 34"><circle cx="17" cy="17" r="17" fill="#ec0a6e"/><path d="M11 14 L17 20 L23 14" stroke="#fff" stroke-width="3" fill="none"/></svg></div>
      <div class="card"><svg width="52" height="52" viewBox="0 0 52 52"><circle cx="26" cy="26" r="24" fill="#fde4ef"/><g stroke="#ec0a6e" stroke-width="3" stroke-linecap="round"><line x1="17" y1="35" x2="35" y2="17"/><line x1="12" y1="32" x2="20" y2="40"/><line x1="32" y1="12" x2="40" y2="20"/></g></svg><h3>3 Weekly Training Sessions<br>For 10 Weeks</h3><p>Training takes place each Tuesday, Thursday and Saturday throughout the 10 week program.</p><svg class="chev" width="34" height="34" viewBox="0 0 34 34"><circle cx="17" cy="17" r="17" fill="#ec0a6e"/><path d="M11 14 L17 20 L23 14" stroke="#fff" stroke-width="3" fill="none"/></svg></div>
      <div class="card"><svg width="52" height="52" viewBox="0 0 52 52"><circle cx="26" cy="26" r="24" fill="#fde4ef"/><g stroke="#ec0a6e" stroke-width="3" stroke-linecap="round"><line x1="17" y1="35" x2="35" y2="17"/><line x1="12" y1="32" x2="20" y2="40"/><line x1="32" y1="12" x2="40" y2="20"/></g></svg><h3>3 Weekly Training Sessions<br>For 10 Weeks</h3><p>Training takes place each Tuesday, Thursday and Saturday throughout the 10 week program.</p><svg class="chev" width="34" height="34" viewBox="0 0 34 34"><circle cx="17" cy="17" r="17" fill="#ec0a6e"/><path d="M11 14 L17 20 L23 14" stroke="#fff" stroke-width="3" fill="none"/></svg></div>
      <div class="card"><svg width="52" height="52" viewBox="0 0 52 52"><circle cx="26" cy="26" r="24" fill="#fde4ef"/><g stroke="#ec0a6e" stroke-width="3" stroke-linecap="round"><line x1="17" y1="35" x2="35" y2="17"/><line x1="12" y1="32" x2="20" y2="40"/><line x1="32" y1="12" x2="40" y2="20"/></g></svg><h3>3 Weekly Training Sessions<br>For 10 Weeks</h3><p>Training takes place each Tuesday, Thursday and Saturday throughout the 10 week program.</p><svg class="chev" width="34" height="34" viewBox="0 0 34 34"><circle cx="17" cy="17" r="17" fill="#ec0a6e"/><path d="M11 14 L17 20 L23 14" stroke="#fff" stroke-width="3" fill="none"/></svg></div>
    </div>
  </div>

  <div class="abs tie-bg"></div>
  <div class="abs tie-img" role="img" aria-label="Boxer in red headgear resting on his stool in the corner between rounds"></div>
  <svg class="abs tie-edge" viewBox="0 0 60 528"><polygon points="41,0 53,0 17,528 5,528" fill="#ec0a6e"/></svg>
  <div class="abs tie-copy">
    <h2>What About The Black<br>Tie Event?</h2>
    <p>After 10 weeks of hard training, it's time to enjoy the big event! The black tie event is a formal two course meal with a four hour beverage package...yes, that includes alcohol.</p>
    <p>Each fighter will have two tables on the night and additional tables are available for purchase where available. Additional tables are strictly limited so get in quickly to avoid missing out on your opportunity to be a part of what is going to be a memorable event.</p>
    <p class="meta">Date: 20 April 2024</p>
    <p class="meta">Dress code: Black Tie (downstairs / tables) – Cocktail (upstairs / general admission)</p>
    <p class="meta">Time: Day Session (approx 12pm start)</p>
  </div>

  <h2 class="sec-title" style="top:3408px">Follow @ Bellmoreshowcaseau</h2>
  <div class="abs tile" style="left:99px;top:3481px;background:linear-gradient(135deg,#3a3a3e,#1a1a1c)" role="img" aria-label="Group training session in the gym"></div>
  <div class="abs tile" style="left:353px;top:3481px;background:linear-gradient(135deg,#5a5550,#222)" role="img" aria-label="Fighters sparring in a training ring"></div>
  <div class="abs tile" style="left:609px;top:3481px;background:linear-gradient(135deg,#1d2a5a,#7a1c24)" role="img" aria-label="Bout on fight night"></div>
  <div class="abs tile" style="left:863px;top:3481px;background:linear-gradient(135deg,#8a1a3a,#2a2a40)" role="img" aria-label="Guests in formal wear at the gala"></div>
  <div class="abs tile" style="left:99px;top:3674px;background:linear-gradient(135deg,#6a6a66,#2a2a2a)" role="img" aria-label="Fighters practising pad work"></div>
  <div class="abs tile" style="left:353px;top:3674px;background:linear-gradient(135deg,#1a1a24,#1c3a7a)" role="img" aria-label="Boxers trading punches under the lights"></div>
  <div class="abs tile" style="left:609px;top:3674px;background:linear-gradient(135deg,#7a2030,#2a1818)" role="img" aria-label="Two fighters posing together at the event"></div>
  <div class="abs tile" style="left:863px;top:3674px;background:linear-gradient(135deg,#3a1216,#1a1a2a)" role="img" aria-label="Boxers in a clinch in the ring"></div>

  <section class="abs contact">
    <h2>Got Any Questions?</h2>
    <p class="sub">Drop Us A Line And Keep In Touch</p>
    <div class="field" style="left:156px;top:149px;width:436px;height:52px">Name*</div>
    <div class="field" style="left:607px;top:149px;width:436px;height:52px">Email Address*</div>
    <div class="field" style="left:156px;top:221px;width:436px;height:52px">Phone*</div>
    <div class="field" style="left:607px;top:221px;width:436px;height:123px">Message*</div>
    <div class="field" style="left:156px;top:292px;width:436px;height:52px"><span style="color:#1a9a3a">◷</span> Perfer Time</div>
    <div class="submit">SUBMIT</div>
  </section>

  <footer class="abs footer">
    <div class="foot-brand">Bellmore<br>Showcase</div>
    <div class="foot-social"><span></span><span></span><span></span><span></span></div>
    <div class="col" style="left:374px;width:230px">
      <h4>Contact Us</h4>
      <div class="row"><span>⌖</span><span>Bellmore, Sample City, QLD,<br>Australia, 4000</span></div>
      <div class="row"><span>✆</span><span>+61 7 3155 0142</span></div>
      <div class="row"><span>✉</span><span>hello@bellmoreshowcase.com.au</span></div>
    </div>
    <div class="col" style="left:627px;width:150px">
      <h4>Quick Links</h4>
      <div>Home</div><div>About The Program</div><div>Meet The Team</div><div>Past Fighters</div><div>Contact Us</div>
    </div>
    <div class="col" style="left:803px;width:300px">
      <h4>Sign For Newsletter</h4>
      <p>Stay connected on new products, events and offers. Valid for new email subscribers only.</p>
      <div class="news-input"><span>Email</span><span class="go"><svg width="18" height="18" viewBox="0 0 18 18"><path d="M2 9 L16 2 L11 16 L9 10 Z" fill="#fff"/></svg></span></div>
    </div>
    <div class="rule"></div>
    <p class="copy">Copyright ©2023 BELLMORESHOWCASE. All Rights Reserved.</p>
  </footer>

</div>
</body>
</html>
```